US Recruiting Firm Needs Dynamic Tri-Fold Brochure

Need tri-fold professional brochure for HR recruiting and consulting firm based in the US.

Target Market(s)

Clients seeking administrative and human resources talent

Industry/Entity Type

Recruitment

Font styles to use
Sans Serif

Requirements
Should not have
• No weird shapes
• No heavy geometric shapes -- I prefer curvy lines
• Not a dark brochure

```html
<!DOCTYPE html>
<html lang="en">
<head>
<meta charset="UTF-8">
<title>Piedmont Talent Partners – Tri-Fold Brochure</title>
<link rel="stylesheet" href="https://fonts.googleapis.com/css2?family=Oswald:wght@400;500;600&family=Open+Sans:wght@400;600;700&display=swap">
<style>
  :root {
    --navy: #2b4a68;
    --navy-deep: #243f5a;
    --lime: #a3c93a;
    --lime-bright: #b5d845;
    --paper: #ffffff;
    --stage: #eeeff1;
    --ink: #26415c;
    --muted: #4f6275;
    --photo-light: #e7ecf1;
    --photo-mid: #b8c3cf;
    --photo-dark: #5b6b7c;
  }
  * { box-sizing: border-box; margin: 0; padding: 0; }
  html, body { width: 1200px; height: 801px; overflow: hidden; background: var(--stage); }
  body { position: relative; font-family: "Open Sans", Arial, sans-serif; }

  .brochure {
    position: absolute; left: 45px; top: 20px;
    width: 1110px; height: 761px;
    display: flex; background: var(--paper);
    box-shadow: 0 6px 24px rgba(0,0,0,.12);
    overflow: hidden;
  }
  .panel { position: relative; width: 370px; height: 100%; }

  /* Services panel */
  .panel-services { background: var(--navy); color: var(--paper); padding: 44px 34px 30px 40px; }
  .services-heading {
    font-weight: 700; font-size: 14px; line-height: 1.3; color: var(--lime-bright);
    text-transform: uppercase; letter-spacing: .3px; margin-bottom: 10px;
  }
  .services-heading.sentence { text-transform: none; font-size: 15px; margin-top: 16px; }
  .services-list { list-style: none; font-size: 12.5px; line-height: 16.4px; }
  .services-list li { padding-left: 14px; position: relative; }
  .services-list li::before {
    content: ""; position: absolute; left: 2px; top: 6px;
    width: 5px; height: 5px; border-radius: 50%; background: var(--paper);
  }

  /* Contact panel */
  .panel-contact { border-left: 1px solid #e4e7ea; }
  .contact-cta {
    position: absolute; top: 44px; left: 0; width: 100%;
    text-align: center; font-family: "Oswald", Arial, sans-serif; font-weight: 500;
    font-size: 20px; line-height: 1.3; color: var(--ink); text-transform: uppercase; z-index: 2;
  }
  .photo {
    position: absolute;
    background: linear-gradient(180deg, var(--photo-light) 0%, var(--photo-mid) 45%, var(--photo-dark) 78%, rgba(255,255,255,0) 100%);
  }
  .photo-meeting { left: 0; top: 140px; width: 370px; height: 360px; }
  .photo-team { left: 0; top: 150px; width: 370px; height: 330px;
    background: linear-gradient(180deg, var(--photo-light) 0%, var(--photo-mid) 40%, var(--photo-dark) 80%, var(--photo-light) 100%); }

  .contact-block { position: absolute; left: 48px; top: 548px; z-index: 2; }
  .contact-title {
    font-family: "Oswald", Arial, sans-serif; font-weight: 600; font-size: 17px;
    letter-spacing: 4px; color: var(--lime); text-transform: uppercase; margin-bottom: 14px;
  }
  .contact-line { display: flex; align-items: center; gap: 12px; font-size: 15px; color: var(--muted); margin-bottom: 10px; }
  .contact-line svg { width: 15px; height: 15px; fill: var(--lime); flex: none; }

  /* Cover panel */
  .panel-cover { border-left: 1px solid #e4e7ea; }
  .brand { position: absolute; top: 50px; left: 0; width: 100%; display: flex; justify-content: center; align-items: center; gap: 10px; z-index: 2; }
  .brand-dot { width: 34px; height: 34px; border-radius: 50%; background: var(--lime); flex: none; }
  .brand-text { text-align: left; }
  .brand-name {
    font-family: "Oswald", Arial, sans-serif; font-weight: 500; font-size: 21px;
    line-height: 1.05; color: var(--navy); text-transform: uppercase;
  }
  .brand-tagline { font-size: 10.5px; color: #333; margin-top: 4px; }
  .cover-specialty {
    position: absolute; top: 498px; left: 0; width: 100%; text-align: center;
    font-family: "Oswald", Arial, sans-serif; font-weight: 600; font-size: 17px;
    line-height: 1.25; color: var(--navy); text-transform: uppercase; z-index: 2;
  }
  .cover-specialty .accent { color: var(--lime); }

  .curve { position: absolute; pointer-events: none; z-index: 1; }
  .curve-top { left: 740px; top: 0; }
  .curve-bottom { left: 370px; top: 500px; }
</style>
</head>
<body>
<main class="brochure">

  <section class="panel panel-services">
    <h2 class="services-heading">We offer stellar HR talent from entry to executive level. Positions that we fill include:</h2>
    <ul class="services-list">
      <li>HR Assistant</li>
      <li>HR Coordinator</li>
      <li>HR Specialist</li>
      <li>HR Generalist</li>
      <li>HR Consultant</li>
      <li>HR Manager</li>
      <li>Employee Relations Specialist</li>
      <li>Employee Relations Manager</li>
      <li>Talent Acquisition Consultant</li>
      <li>Talent Acquisition Specialist</li>
      <li>Recruiter</li>
      <li>Recruiter/HR Generalist</li>
      <li>Benefits Coordinator</li>
      <li>Benefits Specialist</li>
      <li>Compensation Specialist</li>
      <li>Compensation Manager</li>
      <li>Training Specialist</li>
      <li>Learning &amp; Development Consultant</li>
      <li>Diversity and Inclusion Consultant</li>
    </ul>
    <h2 class="services-heading sentence">We provide customized recruiting and consulting services.</h2>
    <ul class="services-list">
      <li>Working with hiring managers on requisitions</li>
      <li>Position &amp; Candidate Profiling</li>
      <li>Sourcing resumes</li>
      <li>Writing and placing job postings</li>
      <li>Screening and interviewing candidates</li>
      <li>Shortlisting Candidates</li>
      <li>Candidate Assessment</li>
      <li>Coordinating Interviews &amp; Debriefing</li>
      <li>Candidate Dispositioning &amp; Updates</li>
      <li>Applicant Tracking</li>
      <li>Job Offers &amp; Salary Negotiation</li>
      <li>Start Date Coordination &amp; Offer Letter</li>
      <li>Onboarding Process / New Hire Paperwork</li>
      <li>New Hire Follow-up &amp; Check-In Surveys</li>
    </ul>
  </section>

  <section class="panel panel-contact">
    <h2 class="contact-cta">To learn more and<br>request a free consultation,<br>contact us today.</h2>
    <div class="photo photo-meeting" role="img" aria-label="Photo of business professionals talking in a bright office with city windows"></div>
    <div class="contact-block">
      <h3 class="contact-title">Contact Us</h3>
      <p class="contact-line">
        <svg viewBox="0 0 24 24" aria-hidden="true"><path d="M6.6 10.8c1.4 2.8 3.8 5.1 6.6 6.6l2.2-2.2c.3-.3.7-.4 1-.2 1.1.4 2.3.6 3.6.6.6 0 1 .4 1 1V20c0 .6-.4 1-1 1C10.6 21 3 13.4 3 4c0-.6.4-1 1-1h3.5c.6 0 1 .4 1 1 0 1.3.2 2.5.6 3.6.1.3 0 .7-.2 1L6.6 10.8z"/></svg>
        555-010-2040
      </p>
      <p class="contact-line">
        <svg viewBox="0 0 24 24" aria-hidden="true"><path d="M2 5h20v14H2z M2 5l10 8 10-8" fill="none" stroke="#a3c93a" stroke-width="2"/><path d="M3 6h18l-9 7z"/></svg>
        hello@piedmonttalent.example
      </p>
      <p class="contact-line">
        <svg viewBox="0 0 24 24" aria-hidden="true"><circle cx="12" cy="12" r="9" fill="none" stroke="#a3c93a" stroke-width="2"/><path d="M3 12h18M12 3c3 3 3 15 0 18M12 3c-3 3-3 15 0 18" fill="none" stroke="#a3c93a" stroke-width="1.6"/></svg>
        www.piedmonttalent.example
      </p>
    </div>
  </section>

  <section class="panel panel-cover">
    <div class="brand">
      <span class="brand-dot" aria-hidden="true"></span>
      <div class="brand-text">
        <p class="brand-name">Piedmont Talent<br>Partners</p>
        <p class="brand-tagline">Human Resources Staffing &amp; Consulting</p>
      </div>
    </div>
    <div class="photo photo-team" role="img" aria-label="Photo of a small team of colleagues reviewing documents together in an office"></div>
    <h2 class="cover-specialty">Specializing in<br><span class="accent">Administrative, Professional,</span><br>and Executive HR Talent</h2>
  </section>

  <svg class="curve curve-top" width="370" height="40" viewBox="0 0 370 40" aria-hidden="true">
    <path d="M0 0 H370 V26 C260 8 130 6 0 18 Z" fill="var(--lime)"/>
  </svg>
  <svg class="curve curve-bottom" width="740" height="261" viewBox="0 0 740 261" aria-hidden="true">
    <path d="M230 261 C380 200 560 150 740 40 V261 Z" fill="var(--navy)"/>
  </svg>
</main>
</body>
</html>
```